Aerospace Center needs app design

We need a design that would be a creative and innovative look of a simple idea connecting air traffic control situations with sonification.
We would like to see designs that use the elements shown in the short video which are different pads, showing 4 different colors, connecting with a degree and feeling of urgency. The different pads will be movable over screen, similar as to a whiteboard where you can move things around. Each of those pads has 4 different elements that are shown:
- ATC Event (you can chose different setups)
- Select a status (you can chose between Information, Caution and Alert. Color needs to feel more alert from Information to Alert.
- Notes box (you can open the box and write additional text on it)
- Music (you can chose different files. on the right side you can see a small group of notes. When you hover over the notes, music will be played without pressing a play or stop button.
The second video is an overview of music archival program that is connected with the pads.
Look and feel
Each slider illustrates characteristics of the customer's brand and the style your logo design should communicate.

```html
<!DOCTYPE html>
<html lang="en">
<head>
<meta charset="utf-8">
<title>ATC Sonification Pads</title>
<link href="https://fonts.googleapis.com/css2?family=Arimo:wght@400;700&display=swap" rel="stylesheet">
<style>
  :root {
    --ink: #000;
    --white: #fff;
    --text-grey: #666;
    --idle-frame: #999;
    --idle-fill: #e3e3e3;
    --idle-row-top: #b4b4b4;
    --idle-row-bottom: #dadada;
    --info-fill: #3dfdbb;
    --info-light: #6cffd0;
    --info-deep: #34dca2;
    --caution-fill: #fffb00;
    --caution-green: #8de25a;
    --caution-lime: #d4f422;
    --caution-orange: #ffa11e;
    --caution-yellow: #ffe414;
    --caution-label: #8ee07a;
    --alert-fill: #ff0a6b;
    --alert-red: #ff3c4e;
    --alert-orange: #ff9a2e;
    --alert-rose: #db2d70;
    --alert-mauve: #c25c8a;
    --alert-music: #8e7a92;
  }
  * { box-sizing: border-box; margin: 0; padding: 0; }
  html, body { width: 1200px; height: 1200px; overflow: hidden; background: var(--white); }
  body { font-family: "Arimo", Arial, sans-serif; position: relative; }

  .state-label {
    position: absolute; font-size: 37px; line-height: 44px; color: var(--ink);
    text-align: center; font-weight: 400;
  }

  .pad {
    position: absolute; width: 274px; height: 368px; border-radius: 32px;
    background: var(--frame);
  }
  .pad::before {
    content: ""; position: absolute; inset: 9px; border: 3px solid var(--white);
    border-radius: 24px; background: var(--fill);
  }
  .pad--idle { --frame: var(--idle-frame); --fill: var(--idle-fill); }
  .pad--info { --frame: var(--info-fill); --fill: var(--info-fill); }
  .pad--caution { --frame: var(--caution-fill); --fill: var(--caution-fill); }
  .pad--alert { --frame: var(--alert-fill); --fill: var(--alert-fill); }

  .pad__id {
    position: absolute; left: 39px; top: 19px; font-size: 28px; font-weight: 700;
    color: var(--white); line-height: 32px;
  }
  .pad--caution .pad__id, .pad--caution .pad__close { color: var(--caution-label); }
  .pad__close {
    position: absolute; left: 217px; top: 14px; font-size: 30px; font-weight: 700;
    color: var(--white); line-height: 32px;
  }

  .pad__row {
    position: absolute; left: 24px; width: 226px; height: 64px; border-radius: 12px;
    color: var(--white); font-weight: 700; font-size: 39px; line-height: 64px;
    padding-left: 10px; white-space: nowrap; overflow: hidden;
  }
  .row--event { top: 58px; }
  .row--status { top: 128px; }
  .row--notes { top: 197px; }
  .row--track { top: 267px; width: 166px; font-size: 25px; }
  .row--music { top: 267px; left: 193px; width: 56px; padding: 0; display: flex; align-items: center; justify-content: center; }

  .pad--idle .pad__row { background: linear-gradient(var(--idle-row-top), var(--idle-row-bottom)); }

  .pad--info .row--event, .pad--info .row--track, .pad--info .row--music { background: var(--info-light); }
  .pad--info .row--status { background: linear-gradient(var(--info-fill), var(--info-deep)); }
  .pad--info .row--notes { background: linear-gradient(var(--info-fill), var(--info-deep)); }

  .pad--caution .row--event { background: linear-gradient(#a7ea5e, var(--caution-green)); }
  .pad--caution .row--status { background: linear-gradient(var(--caution-orange), var(--caution-yellow)); }
  .pad--caution .row--notes, .pad--caution .row--track, .pad--caution .row--music { background: linear-gradient(var(--caution-lime), var(--caution-green)); }

  .pad--alert .row--event { background: linear-gradient(var(--alert-red), var(--alert-orange)); }
  .pad--alert .row--status, .pad--alert .row--notes, .pad--alert .row--track { background: linear-gradient(var(--alert-rose), var(--alert-mauve)); }
  .pad--alert .row--music { background: var(--alert-music); }

  .dropdown {
    position: absolute; background: var(--white); border-radius: 14px;
    box-shadow: 0 8px 0 #3fd9a4;
  }
  .dropdown--event { left: 844px; top: 371px; width: 239px; height: 126px; padding: 6px 0 0 17px; }
  .dropdown__item { font-size: 25px; font-weight: 700; line-height: 27px; color: var(--text-grey); }
  .dropdown__item--muted { color: #e2e2e2; }
  .dropdown--library {
    left: 844px; top: 578px; width: 240px; height: 125px;
    display: flex; align-items: center; justify-content: center;
    font-size: 26px; font-weight: 700; color: var(--text-grey);
    box-shadow: 0 8px 0 #53d5a8;
  }

  .cursor { position: absolute; width: 40px; height: 40px; }
  .sound-waves { position: absolute; left: 700px; top: 470px; }
</style>
</head>
<body>
  <svg width="0" height="0" style="position:absolute">
    <defs>
      <symbol id="pointer" viewBox="0 0 40 40">
        <polygon points="0,0 30,9 20,14 36,30 30,36 14,20 9,30" fill="#000"/>
      </symbol>
      <symbol id="score" viewBox="0 0 48 32">
        <g stroke="#fff" stroke-width="1.5">
          <line x1="0" y1="4" x2="48" y2="4"/>
          <line x1="0" y1="10" x2="48" y2="10"/>
          <line x1="0" y1="16" x2="48" y2="16"/>
          <line x1="0" y1="22" x2="48" y2="22"/>
          <line x1="0" y1="28" x2="48" y2="28"/>
        </g>
        <ellipse cx="19" cy="25" rx="6" ry="4.5" fill="#fff"/>
        <line x1="24" y1="25" x2="24" y2="1" stroke="#fff" stroke-width="2.5"/>
        <path d="M24 1 Q30 6 31 13 Q28 8 24 8 Z" fill="#fff"/>
      </symbol>
    </defs>
  </svg>

  <div class="state-label" style="left:478px; top:153px; width:220px;">on mouse<br>over</div>
  <div class="state-label" style="left:862px; top:175px; width:180px;">on click</div>

  <!-- Idle pad -->
  <div class="pad pad--idle" style="left:119px; top:245px;">
    <span class="pad__id">AB1</span><span class="pad__close">✕</span>
    <div class="pad__row row--event">ATC Event</div>
    <div class="pad__row row--status">Status</div>
    <div class="pad__row row--notes">Notes</div>
    <div class="pad__row row--track"></div>
    <div class="pad__row row--music"><svg width="48" height="32"><use href="#score"/></svg></div>
  </div>

  <!-- Information pad, hover -->
  <div class="pad pad--info" style="left:461px; top:245px;">
    <span class="pad__id">AB1</span><span class="pad__close">✕</span>
    <div class="pad__row row--event">ATC Event</div>
    <div class="pad__row row--status">Information</div>
    <div class="pad__row row--notes">Notes</div>
    <div class="pad__row row--track">Roch..........</div>
    <div class="pad__row row--music"><svg width="48" height="32"><use href="#score"/></svg></div>
  </div>
  <svg class="sound-waves" width="80" height="86" viewBox="0 0 80 86" fill="none" stroke="#000" stroke-width="6">
    <path d="M6 8 A64 64 0 0 1 70 82"/>
    <path d="M12 30 A40 40 0 0 1 50 70"/>
    <path d="M14 50 A20 20 0 0 1 30 68"/>
  </svg>
  <svg class="cursor" style="left:603px; top:329px;"><use href="#pointer"/></svg>
  <svg class="cursor" style="left:674px; top:552px;"><use href="#pointer"/></svg>

  <!-- Information pad, click -->
  <div class="pad pad--info" style="left:827px; top:244px; height:365px;">
    <span class="pad__id">AB1</span><span class="pad__close">✕</span>
    <div class="pad__row row--event">ATC Event</div>
    <div class="pad__row row--status"></div>
    <div class="pad__row row--notes"></div>
    <div class="pad__row row--track">Roch.........</div>
    <div class="pad__row row--music"><svg width="48" height="32"><use href="#score"/></svg></div>
  </div>
  <div class="dropdown dropdown--event">
    <div class="dropdown__item dropdown__item--muted">Event</div>
    <div class="dropdown__item">Landing</div>
    <div class="dropdown__item">Departure</div>
  </div>
  <div class="dropdown dropdown--library">Music library</div>
  <svg class="cursor" style="left:1015px; top:329px;"><use href="#pointer"/></svg>
  <svg class="cursor" style="left:965px; top:547px;"><use href="#pointer"/></svg>

  <!-- Caution pad -->
  <div class="pad pad--caution" style="left:119px; top:691px;">
    <span class="pad__id">AB1</span><span class="pad__close">✕</span>
    <div class="pad__row row--event">ATC Event</div>
    <div class="pad__row row--status">Caution</div>
    <div class="pad__row row--notes">Notes</div>
    <div class="pad__row row--track"></div>
    <div class="pad__row row--music"><svg width="48" height="32"><use href="#score"/></svg></div>
  </div>
  <svg class="cursor" style="left:327px; top:840px;"><use href="#pointer"/></svg>

  <!-- Alert pad -->
  <div class="pad pad--alert" style="left:474px; top:697px;">
    <span class="pad__id">AB1</span><span class="pad__close">✕</span>
    <div class="pad__row row--event">ATC Event</div>
    <div class="pad__row row--status">Alert</div>
    <div class="pad__row row--notes">Notes</div>
    <div class="pad__row row--track"></div>
    <div class="pad__row row--music"><svg width="48" height="32"><use href="#score"/></svg></div>
  </div>
  <svg class="cursor" style="left:649px; top:780px;"><use href="#pointer"/></svg>
</body>
</html>
```